DJQuorbel.com

A clean-looking fun website.

MAP*

top* Video. (To host party footage and also to host live streams as they happen.

Tabs - Events, Livestream, Mixes, Playlists, Sign up, Photos, Bio, Shop

Links to Instagram, Facebook and Twitter, YouTube & Twitch

sign up sheet to take contact details for future promo.

References
http://www.djbrisklomb.com/
http://www.kasperdrune.com/
https://torvinmesk.com/
https://www.djvormaniofficial.com/
https://lenfrask.com/
https://www.samtivvey.com/den/

I hope this helps.

```html
<!DOCTYPE html>
<html lang="en">
<head>
<meta charset="utf-8">
<title>DJ Quorbel</title>
<link href="https://fonts.googleapis.com/css2?family=Oswald:wght@300;400;500;600;700&display=swap" rel="stylesheet">
<style>
:root{
  --brand:#ff3300;
  --brand-deep:#d92a00;
  --ink:#111111;
  --paper:#ffffff;
  --muted:#444444;
  --line:rgba(255,255,255,.55);
}
*{box-sizing:border-box;margin:0;padding:0}
html,body{width:1200px;height:4573px;overflow:hidden}
body{position:relative;background:var(--paper);font-family:'Oswald',sans-serif;color:var(--ink)}
.abs{position:absolute}

/* header */
.site-header{left:0;top:0;width:1200px;height:108px;background:var(--paper)}
.brand-name{left:170px;top:26px;width:176px;height:62px;display:flex;align-items:center;gap:10px;font-size:40px;font-weight:700;color:var(--ink);letter-spacing:1px}
.brand-name .mark{width:18px;height:18px;background:var(--ink)}
.main-nav{left:430px;top:46px;display:flex;gap:17px;font-size:12.5px;font-weight:500;text-transform:uppercase}
.btn{display:flex;align-items:center;justify-content:center;background:var(--brand);color:#fff;font-size:13px;font-weight:500}
.btn-signup{left:935px;top:36px;width:95px;height:38px}

/* hero */
.hero{left:0;top:108px;width:1200px;height:667px;background:radial-gradient(ellipse at 75% 30%,#c86a25 0%,#7a3510 35%,#2a1206 75%,#120804 100%)}
.hero-bar{background:var(--brand-deep)}
.hero-bar-top{left:154px;top:270px;width:396px;height:10px}
.hero-bar-left{left:154px;top:270px;width:10px;height:358px}
.hero-bar-bottom{left:154px;top:618px;width:450px;height:10px}
.hero-kicker{left:199px;top:312px;color:#fff;font-size:23px;font-weight:400;line-height:1.3}
.hero-title{left:195px;top:335px;color:#fff;font-size:100px;font-weight:600;line-height:1.15;white-space:nowrap;letter-spacing:-1px}
.hero-text{left:199px;top:470px;width:430px;color:#fff;font-size:11.5px;line-height:21px}
.btn-contact{left:199px;top:539px;width:147px;height:39px;border:2px solid #fff}
.play-big{left:834px;top:385px;width:126px;height:126px}

/* about */
.about-bar{background:var(--brand)}
.about-bar-top{left:154px;top:896px;width:346px;height:18px}
.about-bar-left{left:154px;top:896px;width:18px;height:492px}
.about-bar-right{left:482px;top:896px;width:18px;height:60px}
.about-bar-bottom{left:154px;top:1370px;width:60px;height:18px}
.about-photo{left:206px;top:946px;width:360px;height:509px;background:linear-gradient(160deg,#8d6bc9 0%,#5e3f87 35%,#3b2b3a 70%,#1f1a1f 100%)}
.about-kicker{left:610px;top:898px;font-size:34px;font-weight:400;line-height:1.2}
.about-title{left:608px;top:940px;font-size:60px;font-weight:600;color:var(--brand);line-height:1.1}
.about-text{left:610px;top:1030px;width:418px;font-size:11.5px;line-height:23px;color:var(--muted)}
.about-text p+p{margin-top:23px}
.btn-detail{left:610px;top:1399px;width:146px;height:37px}

/* livestream */
.livestream{left:0;top:1548px;width:1200px;height:593px;background:linear-gradient(90deg,#10303a 0%,#1a1a2a 45%,#3a1a4a 100%)}
.section-title-light{width:1200px;left:0;text-align:center;color:#fff;font-size:58px;font-weight:600}
.video{left:169px;top:1702px;width:861px;height:369px;border:1px solid #ddd;background:linear-gradient(180deg,#8a2a0a 0%,#c8400c 45%,#ff5a10 70%,#ff3300 100%)}
.video-bar{left:169px;top:2036px;width:861px;height:35px;background:linear-gradient(180deg,#ff4a1a,#c82800)}
.video-time{left:768px;top:2042px;color:#fff;font-size:14px;font-weight:500}
.video-track{left:392px;top:2048px;width:357px;height:11px;border-radius:6px;background:#2a2a2a}
.video-track span{display:block;width:166px;height:100%;border-radius:6px;background:#d8d8d8}

/* events */
.events-kicker{left:0;width:1200px;top:2210px;text-align:center;font-size:36px;font-weight:400}
.events-title{left:0;width:1200px;top:2252px;text-align:center;font-size:60px;font-weight:600;color:var(--brand)}
.event-card{top:2364px;width:272px;height:313px;border:2px solid #f29a9a;text-align:center;background:#fff}
.event-card.is-active{background:var(--brand);border-color:var(--brand);color:#fff}
.event-date{margin:40px auto 0;width:78px;height:74px;background:#fff;box-shadow:2px 3px 4px rgba(0,0,0,.35);color:var(--ink);position:relative;padding-top:8px;line-height:1.05}
.event-date .day{display:block;color:var(--brand);font-size:26px;font-weight:600}
.event-date .mon{display:block;font-size:19px}
.event-date::before,.event-date::after{content:"";position:absolute;top:4px;width:8px;height:8px;border-radius:50%;background:var(--ink)}
.event-date::before{left:10px}.event-date::after{right:10px}
.event-name{margin-top:18px;font-size:23px;font-weight:500}
.event-text{margin:6px auto 0;width:232px;font-size:10.5px;line-height:19px}
.event-time{margin-top:12px;font-size:15px;font-weight:500}
.event-link{display:inline-block;margin-top:18px;font-size:12px;color:var(--brand);text-decoration:underline}
.event-card.is-active .event-link{color:#fff}
.arrow-btn{top:2505px;width:32px;height:32px;background:var(--brand);display:flex;align-items:center;justify-content:center}
.arrow-btn.is-faint{background:#f79a80}

/* playlists */
.playlists{left:0;top:2790px;width:1200px;height:675px;background:radial-gradient(ellipse at 30% 60%,#3a2a1c 0%,#1a120c 45%,#060404 100%)}
.playlist-photo{left:169px;top:2971px;width:420px;height:398px;background:linear-gradient(180deg,#d9d4c8 0%,#9a8e86 28%,#5a4a5a 60%,#1e1a22 100%)}
.play-mid{left:325px;top:3112px;width:104px;height:104px}
.track{left:610px;width:420px;height:100px;border-bottom:3px solid var(--line);color:#fff}
.track .t1{position:absolute;left:1px;top:4px;font-size:21px;font-weight:400}
.track .t2{position:absolute;left:1px;top:36px;font-size:21px;font-weight:400}
.track svg{position:absolute;right:0;top:20px}

/* shop */
.shop-title{left:0;width:1200px;top:3525px;text-align:center;font-size:60px;font-weight:600;color:var(--brand)}
.product{top:3640px;width:199px;text-align:center}
.product-art{width:199px;height:198px;background:#dcdcdc}
.product-name{margin-top:8px;font-size:15px}
.product-price{margin-top:1px;font-size:17px}
.product-link{margin-top:1px;font-size:12px;color:var(--brand);text-decoration:underline}

/* newsletter + footer */
.site-footer{left:0;top:4050px;width:1200px;height:523px;background:linear-gradient(180deg,#0d0d12,#16161c)}
.newsletter{left:169px;top:3981px;width:861px;height:146px;background:var(--brand)}
.newsletter-title{left:220px;top:4005px;color:#fff;font-size:46px;font-weight:500;letter-spacing:-.5px;white-space:nowrap}
.newsletter-text{left:222px;top:4074px;color:#fff;font-size:14px}
.newsletter-input{left:589px;top:4031px;width:388px;height:46px;background:#fff;border:2px solid #fff;display:flex;align-items:center}
.newsletter-input span{padding-left:18px;color:#9a9a9a;font-size:16px;flex:1}
.newsletter-send{width:64px;height:42px;background:var(--brand);display:flex;align-items:center;justify-content:center}
.footer-heading{top:4192px;color:#fff;font-size:28px;font-weight:500;letter-spacing:-.5px}
.contact-list{left:171px;top:4266px;width:240px;color:#fff;font-size:12px;line-height:20px}
.contact-list u{display:block}
.contact-list div+u{margin-top:6px}
.social{top:4432px;width:40px;height:40px;border-radius:50%;border:2px solid #fff}
.social.is-brand{background:var(--brand);border-color:var(--brand)}
.gallery-tile{width:126px;height:68px}
.map{left:756px;top:4251px;width:274px;height:222px;background:linear-gradient(135deg,#eceae4,#d9dbe0)}
.copyright{left:0;top:4537px;width:1200px;height:36px;background:var(--brand);color:#fff;font-size:15px;display:flex;align-items:center;justify-content:center}
</style>
</head>
<body>

<header class="abs site-header">
  <div class="abs brand-name"><span class="mark"></span>quorbel</div>
  <nav class="abs main-nav">
    <span>Home</span><span>About Me</span><span>Events</span><span>Livestream</span><span>Mixes</span><span>Playlists</span><span>Shop</span><span>Contact Us</span>
  </nav>
  <div class="abs btn btn-signup">Sign Up</div>
</header>

<section class="abs hero" role="img" aria-label="Photo of the DJ singing into a microphone at the decks under warm orange stage light"></section>
<div class="abs hero-bar hero-bar-top"></div>
<div class="abs hero-bar hero-bar-left"></div>
<div class="abs hero-bar hero-bar-bottom"></div>
<p class="abs hero-kicker">WELCOME TO</p>
<h1 class="abs hero-title">DJ QUORBEL</h1>
<p class="abs hero-text">Placeholder text is the label for possible content in a text box. It can normally be found when there are prompts to fill out a form.</p>
<div class="abs btn btn-contact">Contact Now</div>
<svg class="abs play-big" viewBox="0 0 128 128"><circle cx="64" cy="64" r="58" fill="none" stroke="#ff3300" stroke-width="10"/><circle cx="64" cy="64" r="48" fill="#111"/><path d="M52 42 L86 64 L52 86 Z" fill="#ff3300"/></svg>

<section>
  <div class="abs about-bar about-bar-top"></div>
  <div class="abs about-bar about-bar-left"></div>
  <div class="abs about-bar about-bar-right"></div>
  <div class="abs about-bar about-bar-bottom"></div>
  <div class="abs about-photo" role="img" aria-label="Photo of the smiling DJ with headphones behind the decks at a party"></div>
  <h2 class="abs about-kicker">About My</h2>
  <h2 class="abs about-title">BIOGRAPHY</h2>
  <div class="abs about-text">
    <p>Placeholder text is the label for possible content in a text box. It can normally be found when there are prompts to fill out a form. It's the hint that tells you 'Last name' or the format with which to enter your birthdate or phone number. Placeholder text typically exists as a hint to fill in actual text.Placeholder text is the label for possible content in a text box. It can normally be found when there are prompts to fill out a form. It's the hint that tells you 'Last name' or the format with which to enter your birthdate or phone number. Placeholder text typically exists as a hint to fill in actual text.</p>
    <p>Placeholder text is the label for possible content in a text box. It can normally be found when there are prompts to fill out a form. It's the hint that tells you 'Last name' or the format with which to enter your birthdate or phone number. Placeholder text typically exists as a hint to fill in actual text.Placeholder text is the label for possible content in a text box. It can normally be found when there are prompts to fill out a form. It's the hint that tells you 'Last name' or the format</p>
  </div>
  <div class="abs btn btn-detail">View Detail</div>
</section>

<section class="abs livestream" role="img" aria-label="Dim background photo of DJ equipment in teal and purple light"></section>
<h2 class="abs section-title-light" style="top:1594px">LIVESTREAM</h2>
<div class="abs video" role="img" aria-label="Live stream video of the DJ performing in front of a crowd with red stage lights"></div>
<svg class="abs" style="left:553px;top:1843px" width="96" height="96" viewBox="0 0 96 96"><circle cx="48" cy="48" r="42" fill="rgba(40,10,0,.45)" stroke="#3a0e00" stroke-width="6"/><path d="M38 30 L66 48 L38 66 Z" fill="#ff3300"/></svg>
<div class="abs video-bar"></div>
<svg class="abs" style="left:290px;top:2043px" width="20" height="22" viewBox="0 0 20 22"><path d="M2 1 L19 11 L2 21 Z" fill="#fff"/></svg>
<svg class="abs" style="left:347px;top:2043px" width="30" height="22" viewBox="0 0 30 22"><path d="M2 7 H8 L15 1 V21 L8 15 H2 Z" fill="#fff"/><path d="M19 7 Q23 11 19 15 M22 4 Q29 11 22 18" stroke="#fff" stroke-width="2" fill="none"/></svg>
<div class="abs video-track"><span></span></div>
<p class="abs video-time">11:57</p>
<p class="abs" style="left:831px;top:2042px;color:#7ad02a;font-size:14px;font-weight:700">HD</p>
<svg class="abs" style="left:882px;top:2043px" width="22" height="22" viewBox="0 0 22 22"><path d="M13 2 H20 V9 M20 2 L13 9 M9 20 H2 V13 M2 20 L9 13" stroke="#fff" stroke-width="2.4" fill="none"/></svg>

<section>
  <h2 class="abs events-kicker">Events</h2>
  <h2 class="abs events-title">UPCOMING DATES</h2>
  <div class="abs arrow-btn" style="left:114px"><svg width="12" height="18" viewBox="0 0 12 18"><path d="M10 2 L3 9 L10 16" stroke="#fff" stroke-width="2.5" fill="none"/></svg></div>
  <article class="abs event-card" style="left:169px">
    <div class="event-date"><span class="day">29</span><span class="mon">Sep</span></div>
    <h3 class="event-name">Corporate Event</h3>
    <p class="event-text">Placeholder text is the label for possible content in a text box. It can normally be found when</p>
    <p class="event-time">8:00 am – 9:00 am</p>
    <span class="event-link">View Detail</span>
  </article>
  <article class="abs event-card is-active" style="left:463px">
    <div class="event-date"><span class="day">11</span><span class="mon">Oct</span></div>
    <h3 class="event-name">Wedding Event</h3>
    <p class="event-text">Placeholder text is the label for possible content in a text box. It can normally be found when</p>
    <p class="event-time">8:00 am – 9:00 am</p>
    <span class="event-link">View Detail</span>
  </article>
  <article class="abs event-card" style="left:758px">
    <div class="event-date"><span class="day">01</span><span class="mon">Nov</span></div>
    <h3 class="event-name">Party Events</h3>
    <p class="event-text">Placeholder text is the label for possible content in a text box. It can normally be found when</p>
    <p class="event-time">8:00 am – 9:00 am</p>
    <span class="event-link">View Detail</span>
  </article>
  <div class="abs arrow-btn is-faint" style="left:1052px"><svg width="12" height="18" viewBox="0 0 12 18"><path d="M2 2 L9 9 L2 16" stroke="#fff" stroke-width="2.5" fill="none"/></svg></div>
</section>

<section class="abs playlists" role="img" aria-label="Dark background photo of a DJ mixing console"></section>
<h2 class="abs section-title-light" style="top:2838px">PLAYLISTS</h2>
<div class="abs playlist-photo" role="img" aria-label="Photo of the DJ and friends on a balcony at a daytime party"></div>
<svg class="abs play-mid" viewBox="0 0 104 104"><circle cx="52" cy="52" r="46" fill="rgba(0,0,0,.35)" stroke="#ff3300" stroke-width="8"/><path d="M42 34 L70 52 L42 70 Z" fill="#ff3300"/></svg>
<div class="abs track" style="top:2978px"><span class="t1">We Exist</span><span class="t2">Perfect Symmetry</span><svg width="44" height="44" viewBox="0 0 44 44"><circle cx="22" cy="22" r="19" fill="none" stroke="#fff" stroke-width="3"/><path d="M17 13 L31 22 L17 31 Z" fill="#fff"/></svg></div>
<div class="abs track" style="top:3083px"><span class="t1">It´s Never Over</span><span class="t2">Perfect Symmetry</span><svg width="44" height="44" viewBox="0 0 44 44"><circle cx="22" cy="22" r="19" fill="none" stroke="#fff" stroke-width="3"/><path d="M17 13 L31 22 L17 31 Z" fill="#fff"/></svg></div>
<div class="abs track" style="top:3188px"><span class="t1">Exploration</span><span class="t2">Perfect Symmetry</span><svg width="44" height="44" viewBox="0 0 44 44"><circle cx="22" cy="22" r="19" fill="none" stroke="#fff" stroke-width="3"/><path d="M17 13 L31 22 L17 31 Z" fill="#fff"/></svg></div>
<div class="abs track" style="top:3293px"><span class="t1">They Return</span><span class="t2">Perfect Symmetry</span><svg width="44" height="44" viewBox="0 0 44 44"><circle cx="22" cy="22" r="19" fill="none" stroke="#fff" stroke-width="3"/><path d="M17 13 L31 22 L17 31 Z" fill="#fff"/></svg></div>

<section>
  <h2 class="abs shop-title">OUR SHOP</h2>
  <div class="abs product" style="left:169px"><div class="product-art" role="img" aria-label="Album cover with pink artwork and a vinyl record" style="background:linear-gradient(90deg,#e2dde0 0%,#e9a8b2 45%,#1a1a1a 75%,#e2dde0 100%)"></div><p class="product-name">Music Album</p><p class="product-price">$29.00</p><p class="product-link">Shop Now</p></div>
  <div class="abs product" style="left:389px"><div class="product-art" role="img" aria-label="Album cover with blue artwork and a vinyl record" style="background:linear-gradient(90deg,#dcdcdc 0%,#5a86b8 40%,#1a1a1a 75%,#dcdcdc 100%)"></div><p class="product-name">Music Album</p><p class="product-price">$29.00</p><p class="product-link">Shop Now</p></div>
  <div class="abs product" style="left:611px"><div class="product-art" role="img" aria-label="Album cover with red and grey artwork and a vinyl record" style="background:linear-gradient(90deg,#dcdcdc 0%,#d8d8d8 20%,#e02020 40%,#1a1a1a 75%,#dcdcdc 100%)"></div><p class="product-name">Music Album</p><p class="product-price">$29.00</p><p class="product-link">Shop Now</p></div>
  <div class="abs product" style="left:831px"><div class="product-art" role="img" aria-label="Album cover with purple and peach artwork and a vinyl record" style="background:linear-gradient(90deg,#dcdcdc 0%,#f0c8a8 25%,#6a3a8a 45%,#1a1a1a 75%,#dcdcdc 100%)"></div><p class="product-name">Music Album</p><p class="product-price">$29.00</p><p class="product-link">Shop Now</p></div>
</section>

<footer class="abs site-footer"></footer>
<div class="abs newsletter"></div>
<h2 class="abs newsletter-title">JOIN MY DJ QUORBEL</h2>
<p class="abs newsletter-text">Enter Your email and be the first to know about events!</p>
<div class="abs newsletter-input"><span>Enter Your Email</span><div class="newsletter-send"><svg width="24" height="22" viewBox="0 0 24 22"><path d="M1 10 L23 1 L17 21 L11 14 Z M11 14 L23 1" fill="#fff" stroke="#ff3300" stroke-width="1"/></svg></div></div>

<h3 class="abs footer-heading" style="left:169px">CONTACT INFO</h3>
<div class="abs contact-list">
  <u>Address:</u><div>Dummy Street 123, Road XYZ<br>Placeholder text</div>
  <u>Call Us:</u><div>123-456-7890</div>
  <u>Email Address:</u><div>yourdomain@mailbox.com</div>
</div>
<div class="abs social is-brand" style="left:170px" aria-label="Social link"></div>
<div class="abs social" style="left:221px" aria-label="Social link"></div>
<div class="abs social" style="left:271px" aria-label="Social link"></div>
<div class="abs social" style="left:323px" aria-label="Social link"></div>

<h3 class="abs footer-heading" style="left:433px">OUR GALLERY</h3>
<div class="abs gallery-tile" style="left:433px;top:4251px;background:linear-gradient(135deg,#1a8a9a,#0a2a3a)" role="img" aria-label="Party photo in teal light"></div>
<div class="abs gallery-tile" style="left:574px;top:4251px;background:linear-gradient(135deg,#3a4ad0,#0a0a3a)" role="img" aria-label="Party photo in blue light"></div>
<div class="abs gallery-tile" style="left:433px;top:4328px;background:linear-gradient(135deg,#c82aa0,#2a0a3a)" role="img" aria-label="Crowd photo in magenta light"></div>
<div class="abs gallery-tile" style="left:574px;top:4328px;background:linear-gradient(135deg,#2ab03a,#0a2a1a)" role="img" aria-label="DJ photo in green light"></div>
<div class="abs gallery-tile" style="left:433px;top:4405px;background:linear-gradient(135deg,#e04a8a,#1a0a2a)" role="img" aria-label="Club photo in pink light"></div>
<div class="abs gallery-tile" style="left:574px;top:4405px;background:linear-gradient(135deg,#6a3ad0,#0a0a2a)" role="img" aria-label="DJ photo in purple light"></div>

<h3 class="abs footer-heading" style="left:756px">OUR LOCATION</h3>
<div class="abs map" role="img" aria-label="Street map showing the studio location"></div>
<svg class="abs" style="left:881px;top:4327px" width="24" height="34" viewBox="0 0 24 34"><path d="M12 1 C5 1 1 6 1 12 C1 20 12 33 12 33 C12 33 23 20 23 12 C23 6 19 1 12 1 Z" fill="#ff3300"/><circle cx="12" cy="12" r="4.5" fill="#fff"/></svg>

<div class="abs copyright">Copyright © 2021. All Rights Reserved.</div>

</body>
</html>
```